Veltrium stationery design

Design stationery for us that fits with the colours of the logo. We are looking for letterheads, business cards etc. Something we can use for a prospectus and marketing presentations in power point. Must be completed in such a manner that it represents a corporate image for large enterprise clients and other large organisations. The company is a project assurance and monitoring company that works in all industries.

```html
<!DOCTYPE html>
<html lang="en">
<head>
<meta charset="utf-8">
<title>Veltrium Stationery</title>
<link href="https://fonts.googleapis.com/css2?family=Montserrat:wght@500;600;700;800&display=swap" rel="stylesheet">
<style>
:root{
  --navy:#1f3a72;
  --navy-deep:#172d5a;
  --orange:#ea5d1c;
  --red:#c8302a;
  --paper:#ffffff;
  --ground:#e4e5e7;
  --ink:#2b3550;
  --muted:#6a7287;
}
*{box-sizing:border-box;margin:0;padding:0}
html,body{width:1200px;height:797px;overflow:hidden}
body{background:var(--ground);font-family:'Montserrat',sans-serif;color:var(--ink);position:relative}
.piece{position:absolute;box-shadow:0 6px 18px rgba(0,0,0,.12)}
.brand{font-weight:700;letter-spacing:.04em;display:flex;align-items:center;gap:8px;text-transform:uppercase}
.brand .dot{width:14px;height:14px;border-radius:50%;background:var(--orange);flex:none}
.brand--navy{color:var(--navy)}
.brand--white{color:#fff}

/* Letterhead */
.letterhead{left:40px;top:60px;width:440px;height:622px;background:var(--paper)}
.letterhead__head{position:absolute;left:36px;top:40px;right:36px}
.letterhead__head .brand{font-size:22px}
.letterhead__contact{margin-top:10px;padding-bottom:8px;border-bottom:1.5px solid var(--navy);font-size:8.5px;font-weight:500;color:var(--navy)}
.letterhead__accent{position:absolute;left:0;right:0;bottom:46px;height:8px;background:linear-gradient(90deg,var(--navy) 0%,var(--navy) 35%,var(--red) 70%,var(--orange) 100%)}
.letterhead__band{position:absolute;left:0;right:0;bottom:0;height:46px;background:var(--navy);color:#fff;font-size:9px;font-weight:600;letter-spacing:.06em;display:flex;align-items:center;justify-content:center}

/* Business cards */
.card{left:510px;width:240px;height:137px}
.card--logo{top:60px;background:var(--paper);display:flex;align-items:center;justify-content:center}
.card--logo .brand{font-size:20px}
.card--back{background:var(--navy);display:flex;flex-direction:column;align-items:center;justify-content:center;gap:16px}
.card--back .brand{font-size:20px}
.card--back .web{color:#fff;font-size:9px;font-weight:500;letter-spacing:.05em}
.card--back-a{top:213px}
.card--back-b{top:366px}
.card--contact{top:519px;background:var(--paper);padding:18px 18px 0}
.card--contact .brand{font-size:16px}
.card__body{display:flex;margin-top:14px;gap:12px}
.card__person{flex:1;align-self:flex-end}
.card__name{font-size:13px;font-weight:800;color:var(--navy);text-transform:uppercase}
.card__role{font-size:7.5px;font-weight:600;color:var(--navy);text-transform:uppercase;margin-top:2px}
.card__details{border-left:1.5px solid var(--orange);padding-left:10px;font-size:7.5px;line-height:1.45;color:var(--navy);font-weight:500}
.card__stripe{position:absolute;left:0;right:0;bottom:0;height:7px;background:linear-gradient(90deg,var(--navy) 55%,var(--orange))}

/* Slide */
.slide{left:780px;top:60px;width:380px;height:214px;background:var(--paper);border:8px solid #1c1d21;border-radius:12px;overflow:hidden}
.slide__label{position:absolute;left:18px;top:12px;font-size:7px;font-weight:700;color:var(--navy);letter-spacing:.08em;border-bottom:1px solid var(--navy);padding-bottom:3px;width:110px}
.slide__title{position:absolute;left:18px;top:58px;font-size:20px;line-height:1.08;font-weight:800;color:var(--navy);text-transform:uppercase}
.slide__chart{position:absolute;right:14px;top:10px}
.slide__brand{position:absolute;right:16px;bottom:34px;font-size:10px}
.slide__brand .dot{width:9px;height:9px}
.slide__footer{position:absolute;left:18px;bottom:14px;font-size:6px;color:var(--muted)}
.slide__strip{position:absolute;right:0;bottom:0;width:150px;height:5px;background:linear-gradient(90deg,var(--orange),var(--navy))}

/* Brochure */
.brochure{left:780px;top:300px;width:250px;height:353px;background:var(--paper);overflow:hidden}
.brochure__head{position:absolute;left:16px;top:24px}
.brochure__head .brand{font-size:15px}
.brochure__head .dot{width:11px;height:11px}
.brochure__photo{position:absolute;inset:0;background:linear-gradient(170deg,#9fb2c8 0%,#6b819c 35%,#4a5a6e 60%,#6e6f6a 85%,#8a7d63 100%)}
.brochure__shapes{position:absolute;inset:0}
.brochure__title{position:absolute;left:18px;top:142px;width:210px;color:#fff;font-size:17px;line-height:1.12;font-weight:800;text-transform:uppercase}

/* Notebook */
.notebook{left:1050px;top:300px;width:110px;height:170px;background:var(--navy);border-radius:3px 8px 8px 3px}
.notebook__band{position:absolute;right:12px;top:0;bottom:0;width:6px;background:var(--navy-deep)}
.notebook__brand{position:absolute;left:0;right:18px;top:60px;justify-content:center;font-size:11px}
.notebook__brand .dot{width:9px;height:9px}
.notebook__label{position:absolute;left:0;right:18px;bottom:24px;text-align:center;color:#fff;font-size:7.5px;font-weight:600;letter-spacing:.08em}
</style>
</head>
<body>

<section class="piece letterhead">
  <header class="letterhead__head">
    <div class="brand brand--navy"><span class="dot"></span>Veltrium</div>
    <p class="letterhead__contact">123 Business Avenue, City, State, ZIP &nbsp;|&nbsp; +1 (555) 123-4567 &nbsp;|&nbsp; contact@veltrium.com</p>
  </header>
  <div class="letterhead__accent"></div>
  <footer class="letterhead__band">PROJECT ASSURANCE | PERFORMANCE MONITORING | GOVERNANCE | ACROSS ALL INDUSTRIES</footer>
</section>

<section class="piece card card--logo">
  <div class="brand brand--navy"><span class="dot"></span>Veltrium</div>
</section>

<section class="piece card card--back card--back-a">
  <div class="brand brand--white"><span class="dot"></span>Veltrium</div>
  <p class="web">www.veltrium.com</p>
</section>

<section class="piece card card--back card--back-b">
  <div class="brand brand--white"><span class="dot"></span>Veltrium</div>
  <p class="web">www.veltrium.com</p>
</section>

<section class="piece card card--contact">
  <div class="brand brand--navy"><span class="dot"></span>Veltrium</div>
  <div class="card__body">
    <div class="card__person">
      <p class="card__name">Mara Lind</p>
      <p class="card__role">Managing Director</p>
    </div>
    <p class="card__details">123 Business Avenue,<br>City, State, ZIP<br>+1 (555) 123-4567<br>contact@veltrium.com</p>
  </div>
  <div class="card__stripe"></div>
</section>

<section class="piece slide">
  <p class="slide__label">POWERPOINT</p>
  <h1 class="slide__title">Q3 Project<br>Monitoring<br>Overview</h1>
  <svg class="slide__chart" width="150" height="100" viewBox="0 0 150 100" aria-label="Quarterly bar chart">
    <g stroke="#d7dbe3" stroke-width=".6">
      <line x1="18" y1="12" x2="148" y2="12"/><line x1="18" y1="32" x2="148" y2="32"/>
      <line x1="18" y1="52" x2="148" y2="52"/><line x1="18" y1="72" x2="148" y2="72"/>
      <line x1="18" y1="88" x2="148" y2="88"/>
    </g>
    <g fill="#1f3a72">
      <rect x="24" y="58" width="9" height="30"/><rect x="50" y="44" width="9" height="44"/>
      <rect x="76" y="36" width="9" height="52"/><rect x="102" y="26" width="9" height="62"/>
      <rect x="128" y="18" width="9" height="70"/>
    </g>
    <g fill="#ea5d1c">
      <rect x="34" y="66" width="9" height="22"/><rect x="60" y="38" width="9" height="50"/>
      <rect x="86" y="22" width="9" height="66"/><rect x="112" y="14" width="9" height="74"/>
      <rect x="138" y="30" width="9" height="58"/>
    </g>
    <polyline points="28,60 54,46 80,30 106,18 132,10" fill="none" stroke="#c8302a" stroke-width="1.4"/>
    <g fill="#6a7287" font-size="5" font-family="Montserrat, sans-serif">
      <text x="26" y="96">2019</text><text x="52" y="96">2020</text><text x="78" y="96">2021</text>
      <text x="104" y="96">2022</text><text x="130" y="96">2023</text>
    </g>
  </svg>
  <div class="brand brand--navy slide__brand"><span class="dot"></span>Veltrium</div>
  <p class="slide__footer">123 Business Avenue, City | contact@veltrium.com</p>
  <div class="slide__strip"></div>
</section>

<section class="piece brochure">
  <div class="brochure__photo" role="img" aria-label="Photo of a city skyline with elevated highway interchanges at dusk"></div>
  <svg class="brochure__shapes" width="250" height="353" viewBox="0 0 250 353" aria-hidden="true">
    <polygon points="0,0 130,0 0,90" fill="#ffffff"/>
    <polygon points="0,0 250,0 250,30 0,90" fill="#ffffff" fill-opacity=".0"/>
    <polygon points="0,0 120,0 0,80" fill="#ffffff"/>
    <polygon points="0,70 120,0 250,0 250,8 0,78" fill="#ffffff"/>
    <polygon points="0,110 250,60 250,190 0,245" fill="#1f3a72" fill-opacity=".88"/>
    <polygon points="0,245 250,190 250,196 0,251" fill="#ea5d1c"/>
    <polygon points="180,75 250,60 250,130" fill="#ea5d1c" fill-opacity=".85"/>
  </svg>
  <div class="brochure__head"><div class="brand brand--navy"><span class="dot"></span>Veltrium</div></div>
  <h2 class="brochure__title">Optimizing<br>Project Success<br>Across All<br>Industries</h2>
</section>

<section class="piece notebook">
  <div class="brand brand--white notebook__brand"><span class="dot"></span>Veltrium</div>
  <p class="notebook__label">PROJECT LOG</p>
  <div class="notebook__band"></div>
</section>

</body>
</html>
```